Instagram Posts for a restaurants

We need 5-10 Instagram posts for a restaurant located in Dubai, UAE.

Background about the restaurant:

Forks and Pails is a boutique burgers and comfort food joint located at Dubai, UAE. We started operations in September 2016. The main focus on our food is for it to be simple, original and freshly made. The majority of our orders are take away with fewer people opting for dinning in. We connect with our customers through our Instagram account & our customers rely on it for updates.

The brief

What we are looking for is a vector design (advertisement) for multiple purposes including:

1. announcing that we started delivery
2. a post that we can use multiple times during the year just as a "reminder that we deliver"
3. posts that serve as an advertisement

posts need to be as simple as possible

for reference, our Instagram account is @forksandpails

Industry/Entity Type

Restaurant

Colors
f04a50
ffffff
000000

Requirements
Should not have
• the designs should not have too many colors

```html
<!DOCTYPE html>
<html lang="en">
<head>
<meta charset="utf-8">
<title>Forks and Pails — Instagram posts</title>
<link rel="stylesheet" href="https://fonts.googleapis.com/css2?family=Quicksand:wght@700&display=swap">
<style>
  :root {
    --backdrop: #d8d8d8;
    --post-bg: #ffffff;
    --brand-red: #e8312f;
    --ink: #1e1e1e;
  }
  html, body {
    margin: 0;
    padding: 0;
    width: 1200px;
    height: 1200px;
    overflow: hidden;
    background: var(--backdrop);
    font-family: "Quicksand", "Helvetica Neue", Arial, sans-serif;
  }
  .post-series {
    position: absolute;
    top: 400px;
    left: 38px;
    display: flex;
    gap: 46px;
  }
  .post {
    width: 340px;
    height: 380px;
    background: var(--post-bg);
    box-shadow: 0 6px 14px rgba(0,0,0,0.12);
    display: flex;
    flex-direction: column;
    align-items: center;
    justify-content: center;
    box-sizing: border-box;
    padding-bottom: 20px;
  }
  .post-illustration {
    background: var(--brand-red);
    border-radius: 22px;
    margin-bottom: 26px;
  }
  .post-illustration--burger-fast { width: 116px; height: 58px; }
  .post-illustration--cone { width: 54px; height: 98px; border-radius: 10px 10px 27px 27px; }
  .post-illustration--burger-shine { width: 160px; height: 64px; }
  .post-headline {
    margin: 0;
    color: var(--ink);
    font-size: 46px;
    line-height: 48px;
    font-weight: 700;
    text-align: center;
    letter-spacing: 0.5px;
  }
</style>
</head>
<body>
  <main class="post-series">
    <article class="post">
      <div class="post-illustration post-illustration--burger-fast" role="img" aria-label="Red burger illustration with speed lines"></div>
      <h2 class="post-headline">we delivery<br>to you</h2>
    </article>
    <article class="post">
      <div class="post-illustration post-illustration--cone" role="img" aria-label="Red paper cone filled with fries"></div>
      <h2 class="post-headline">we serve<br>in cones</h2>
    </article>
    <article class="post">
      <div class="post-illustration post-illustration--burger-shine" role="img" aria-label="Red burger illustration with radiating lines"></div>
      <h2 class="post-headline">simple<br>original</h2>
    </article>
  </main>
</body>
</html>
```